Coffee bag stamp design for new coffee brand

Stamp design that will be used like a label on a coffee package.
It must be a vector that can be produced as a stamp. Coffee bag is from brown craft paper. I upload image of this bag. Size of design is 80mm x 140mm.
I also uploaded two pictures for inspiration, but I will also appreciate new ideas.

Target Market(s)

Coffee lovers, who love to try new coffee. Also hipsters.

Colors

Designer to choose only greyscale colors for use in the design.

Requirements
Must have
• Some information about coffee must have:
Name: BRAZIL (the biggest font in that design)
Region: Santos
Altitude: 60 – 1200 m.n.m.
Variety: Arabica
Processing: unwashed

```html
<!DOCTYPE html>
<html lang="en">
<head>
<meta charset="UTF-8">
<title>Brazil – Coffee Bag Stamp</title>
<link rel="stylesheet" href="https://fonts.googleapis.com/css2?family=Montserrat:wght@400;600;700&display=swap">
<style>
  :root {
    --paper: #e3e3e3;
    --ink: #333333;
    --ink-soft: #3f3f3f;
    --ornament-light: #d6d6d6;
    --ornament-dark: #bdbdbd;
    --tab-text: #f2f2f2;
  }
  * { margin: 0; padding: 0; box-sizing: border-box; }
  html, body {
    width: 1200px;
    height: 800px;
    overflow: hidden;
    background: var(--paper);
    font-family: "Montserrat", sans-serif;
    color: var(--ink);
  }
  .canvas {
    position: relative;
    width: 1200px;
    height: 800px;
  }
  .stamp {
    position: absolute;
    left: 428px;
    top: 100px;
    width: 345px;
    height: 600px;
  }
  .mandala {
    position: absolute;
    left: 8px;
    top: 0;
    width: 332px;
    height: 305px;
    border-radius: 48% 48% 8px 8px;
    background: radial-gradient(circle at 50% 62%, var(--ornament-dark) 0%, var(--ornament-light) 55%, var(--paper) 100%);
  }
  .brand-mark {
    position: absolute;
    left: 0;
    width: 345px;
    top: 200px;
    text-align: center;
    font-weight: 700;
    font-size: 20px;
    line-height: 1.1;
    letter-spacing: 0.5px;
    color: var(--ink);
  }
  .rule {
    position: absolute;
    left: 0;
    width: 345px;
    background: var(--ink);
  }
  .rule--heavy { height: 5px; }
  .rule--thin { height: 1.5px; background: var(--ink-soft); }
  .origin-name {
    position: absolute;
    left: 0;
    width: 345px;
    top: 318px;
    text-align: center;
    font-weight: 600;
    font-size: 80px;
    line-height: 1;
    letter-spacing: 2px;
  }
  .spec {
    position: absolute;
    top: 0;
    display: flex;
    flex-direction: column;
    gap: 4px;
  }
  .spec--left { left: 18px; text-align: left; }
  .spec--right { right: 18px; text-align: right; }
  .spec__label {
    font-weight: 400;
    font-size: 15px;
    letter-spacing: 0.3px;
    text-transform: uppercase;
  }
  .spec__value {
    font-weight: 700;
    font-size: 18px;
    letter-spacing: 0.5px;
    text-transform: uppercase;
  }
  .spec-row {
    position: absolute;
    left: 0;
    width: 345px;
    height: 50px;
  }
  .weight-tab {
    position: absolute;
    left: 110px;
    top: 559px;
    width: 125px;
    height: 41px;
    background: var(--ink);
    color: var(--tab-text);
    border-radius: 0 0 10px 10px;
    display: flex;
    align-items: center;
    justify-content: center;
    font-weight: 700;
    font-size: 19px;
    letter-spacing: 0.5px;
  }
</style>
</head>
<body>
  <main class="canvas">
    <section class="stamp">
      <div class="mandala" role="img" aria-label="Line-drawn lotus mandala ornament framing the brand name"></div>
      <div class="brand-mark">ANJALI<br>COFFEE</div>

      <div class="rule rule--heavy" style="top:310px"></div>
      <h1 class="origin-name">BRAZIL</h1>
      <div class="rule rule--heavy" style="top:413px"></div>

      <div class="spec-row" style="top:432px">
        <div class="spec spec--left">
          <span class="spec__label">Region</span>
          <span class="spec__value">Santos</span>
        </div>
        <div class="spec spec--right">
          <span class="spec__label">Altitude</span>
          <span class="spec__value">60 – 1200 m.n.m.</span>
        </div>
      </div>
      <div class="rule rule--thin" style="top:487px"></div>

      <div class="spec-row" style="top:500px">
        <div class="spec spec--left">
          <span class="spec__label">Variety</span>
          <span class="spec__value">Arabica</span>
        </div>
        <div class="spec spec--right">
          <span class="spec__label">Process</span>
          <span class="spec__value">Unwashed</span>
        </div>
      </div>
      <div class="rule rule--thin" style="top:558px"></div>

      <div class="weight-tab">250 G</div>
    </section>
  </main>
</body>
</html>
```